Photoshop Design

Hi, you did a project for me a while ago as per the below description. Can you do the same again with this screen shot?
"We have a charting software application and we are in the process of upgrading our marketing.
We need our application charting screen re-created in photoshop with all components on separate layers so we can tinker with them later such as highlight particular components we are discussing and the likes.
We need the native photoshop file as the project output"
Target Market(s)
Myself
Requirements
Must have
- Look like the sample provided with layers for later editing.

```html
<!DOCTYPE html>
<html lang="en">
<head>
<meta charset="utf-8">
<title>Test Health</title>
<link rel="stylesheet" href="https://fonts.googleapis.com/css2?family=Open+Sans:wght@400;600;700&family=Share+Tech+Mono&display=swap">
<style>
  :root {
    --bg: #262626;
    --panel: #2f2f2f;
    --panel-dark: #1e1e1e;
    --dial: #1d1d1d;
    --dial-inner: #262626;
    --plot: #121212;
    --band: #0f2a33;
    --accent: #1a8be0;
    --accent-deep: #0c69a6;
    --cyan: #12b4ee;
    --green: #22dd22;
    --red: #e0202a;
    --pink: #e2267a;
    --text: #e6e6e6;
    --muted: #9a9a9a;
    --tick: #8a8a8a;
    --button: #333333;
    --callout: #ffee00;
    --marker: #f0a020;
  }
  html, body { margin: 0; padding: 0; overflow: hidden; background: var(--bg); }
  .viewport { width: 1200px; height: 653px; overflow: hidden; position: relative; }
  .stage {
    width: 1500px; height: 816px; position: absolute; left: 0; top: 0;
    transform: scale(0.8); transform-origin: 0 0;
    background: var(--bg);
    font-family: "Open Sans", Arial, sans-serif; color: var(--text);
  }
  .side-label {
    position: absolute; top: 36px; writing-mode: vertical-rl;
    color: var(--accent); font-size: 13px; letter-spacing: .3px;
  }
  .side-label.main-menu { left: 10px; }
  .side-label.controls { left: 1474px; }
  .round-icon {
    position: absolute; width: 18px; height: 18px; border-radius: 50%;
    background: #fff;
  }
  .round-icon svg { display: block; }
  .icon-back { left: 9px; top: 9px; }
  .icon-up { left: 46px; top: 9px; }
  .icon-forward { left: 1473px; top: 9px; }
  .page-title {
    position: absolute; left: 72px; top: 10px; font-size: 13px; color: var(--accent);
  }
  .gauge-panel { position: absolute; left: 37px; top: 37px; width: 1298px; height: 236px; background: var(--panel); }
  .chart-panel { position: absolute; left: 37px; top: 275px; width: 1298px; height: 541px; background: #2b2b2b; }
  .artwork { position: absolute; left: 0; top: 0; }
  .control-panel {
    position: absolute; left: 1338px; top: 3px; width: 124px; height: 342px; background: #2c2c2c;
  }
  .control-panel.lower { top: 692px; height: 121px; }
  .control-button {
    position: absolute; left: 5px; width: 114px; height: 50px; background: var(--button);
    display: flex; align-items: center; justify-content: center; text-align: center;
    font-size: 16px; color: var(--text); line-height: 1.35;
  }
  .control-button.active { background: var(--accent-deep); color: #fff; }
  .control-button.disabled { background: #232323; color: #3e3e3e; }
  svg text { font-family: "Open Sans", Arial, sans-serif; }
  .digits { font-family: "Share Tech Mono", monospace; }
</style>
</head>
<body>
<div class="viewport">
<div class="stage">

  <div class="round-icon icon-back"><svg width="18" height="18"><path d="M10.5 5 L6 9 L10.5 13 Z" fill="#222"/></svg></div>
  <div class="round-icon icon-up"><svg width="18" height="18"><path d="M5 11 L9 6.5 L13 11 Z" fill="#222"/></svg></div>
  <div class="round-icon icon-forward"><svg width="18" height="18"><path d="M7.5 5 L12 9 L7.5 13 Z" fill="#222"/></svg></div>
  <div class="page-title">Test Health</div>
  <div class="side-label main-menu">Main Menu</div>
  <div class="side-label controls">Controls</div>

  <div class="gauge-panel"></div>
  <div class="chart-panel"></div>

  <svg class="artwork" width="1500" height="816" viewBox="0 0 1500 816">
    <defs>
      <pattern id="digit-cells" width="29" height="10" patternUnits="userSpaceOnUse">
        <rect width="27" height="10" fill="#2a2a2a"/>
        <rect x="27" width="2" height="10" fill="#1c1c1c"/>
      </pattern>
      <g id="dial-ticks">
        <path d="M -56.45 63.55 A 85 85 0 1 1 56.45 63.55" fill="none" stroke="var(--tick)" stroke-width="6"
              pathLength="41" stroke-dasharray="0.07 0.93" stroke-dashoffset="-0.465"/>
        <path d="M -40.07 74.96 A 85 85 0 1 1 40.07 74.96" fill="none" stroke="var(--tick)" stroke-width="12"
              pathLength="9" stroke-dasharray="0.025 0.975" stroke-dashoffset="-0.4875"/>
      </g>
      <g id="dial-body">
        <circle r="112" fill="var(--dial)"/>
        <circle r="76" fill="var(--dial-inner)"/>
      </g>
      <g id="spec-pointer">
        <path d="M -6 -59 L 0 -70 L 6 -59 Z" fill="#cfcfcf"/>
        <text y="-52" text-anchor="middle" font-size="7.5" fill="#cfcfcf">TEST SPEC</text>
      </g>
    </defs>

    <!-- Sensor readout -->
    <g class="sensor-readout">
      <text x="165" y="99" text-anchor="middle" font-size="19" fill="#bdbdbd">SENSOR</text>
      <rect x="52" y="106" width="250" height="98" rx="16" fill="var(--panel-dark)"/>
      <rect x="65" y="118" width="230" height="72" rx="8" fill="url(#digit-cells)"/>
      <text x="122" y="174" class="digits" font-size="54" fill="var(--accent)">839</text>
      <rect x="218" y="168" width="8" height="8" fill="var(--accent)"/>
      <text x="237" y="174" class="digits" font-size="54" fill="var(--accent)">0</text>
    </g>

    <!-- Sensor gauge -->
    <g class="gauge sensor-gauge" transform="translate(390 155)">
      <use href="#dial-body"/>
      <circle r="76" fill="var(--dial-inner)"/>
      <path d="M -55.15 55.15 A 78 78 0 1 1 55.15 55.15" fill="none" stroke="var(--cyan)" stroke-width="12"
            pathLength="1100" stroke-dasharray="590 2000"/>
      <path d="M -55.15 55.15 A 78 78 0 1 1 55.15 55.15" fill="none" stroke="var(--green)" stroke-width="12"
            pathLength="1100" stroke-dasharray="0 590 250 2000"/>
      <path d="M -49.5 49.5 A 70 70 0 1 1 49.5 49.5" fill="none" stroke="var(--green)" stroke-width="2"
            pathLength="1100" stroke-dasharray="0 580 280 2000"/>
      <path d="M -49.5 49.5 A 70 70 0 1 1 49.5 49.5" fill="none" stroke="var(--cyan)" stroke-width="2"
            pathLength="1100" stroke-dasharray="580 2000"/>
      <path d="M -49.5 49.5 A 70 70 0 1 1 49.5 49.5" fill="none" stroke="var(--red)" stroke-width="4"
            pathLength="1100" stroke-dasharray="0 940 80 2000"/>
      <path d="M -60.8 60.8 A 86 86 0 1 1 60.8 60.8" fill="none" stroke="var(--tick)" stroke-width="5"
            pathLength="41" stroke-dasharray="0.07 0.93" stroke-dashoffset="-0.465" transform="scale(1.05)"/>
      <g font-size="9" fill="#d0d0d0" text-anchor="middle">
        <text transform="rotate(-135) translate(0 -99)">0</text>
        <text transform="rotate(-101.25) translate(0 -99)">138</text>
        <text transform="rotate(-67.5) translate(0 -99)">275</text>
        <text transform="rotate(-33.75) translate(0 -99)">413</text>
        <text transform="rotate(0) translate(0 -99)">550</text>
        <text transform="rotate(33.75) translate(0 -99)">688</text>
        <text transform="rotate(67.5) translate(0 -99)">825</text>
        <text transform="rotate(101.25) translate(0 -99)">963</text>
        <text transform="rotate(135) translate(0 -99)">1100</text>
      </g>
      <line x1="0" y1="0" x2="0" y2="-72" stroke="#c8c8c8" stroke-width="2.5" transform="rotate(70.9)"/>
      <circle r="16" fill="#232323" stroke="#9a9a9a" stroke-width="2"/>
      <line x1="-28" y1="3" x2="0" y2="0" stroke="#9a9a9a" stroke-width="2"/>
      <text y="49" text-anchor="middle" font-size="19" fill="#cfcfcf">psi</text>
      <rect x="-33" y="64" width="66" height="21" rx="5" fill="url(#digit-cells)"/>
      <text x="-18" y="81" class="digits" font-size="19" fill="var(--pink)">30</text>
      <rect x="6" y="77" width="3" height="3" fill="var(--pink)"/>
      <text x="13" y="81" class="digits" font-size="19" fill="var(--pink)">1</text>
      <text y="98" text-anchor="middle" font-size="11" fill="#cfcfcf">deg C</text>
    </g>

    <!-- Change gauge -->
    <g class="gauge change-gauge" transform="translate(627 155)">
      <use href="#dial-body"/>
      <use href="#dial-ticks"/>
      <path d="M -59.4 59.4 A 84 84 0 1 1 59.4 59.4" fill="none" stroke="var(--green)" stroke-width="12"
            pathLength="270" stroke-dasharray="0 134 12 400"/>
      <g font-size="9" fill="#d0d0d0" text-anchor="middle">
        <text transform="rotate(-135) translate(0 -99)">-70</text>
        <text transform="rotate(-101.25) translate(0 -99)">-55</text>
        <text transform="rotate(-67.5) translate(0 -99)">-40</text>
        <text transform="rotate(-33.75) translate(0 -99)">-25</text>
        <text transform="rotate(0) translate(0 -99)">-10</text>
        <text transform="rotate(33.75) translate(0 -99)">5</text>
        <text transform="rotate(67.5) translate(0 -99)">20</text>
        <text transform="rotate(101.25) translate(0 -99)">35</text>
        <text transform="rotate(135) translate(0 -99)">50</text>
      </g>
      <use href="#spec-pointer"/>
      <text y="-28" text-anchor="middle" font-size="19" fill="#dcdcdc">CHANGE</text>
      <rect x="-61" y="-22" width="122" height="45" rx="8" fill="url(#digit-cells)"/>
      <text x="-8" y="12" text-anchor="middle" class="digits" font-size="34" fill="#f0f0f0">-5</text>
      <rect x="15" y="6" width="5" height="5" fill="#f0f0f0"/>
      <text x="36" y="12" text-anchor="middle" class="digits" font-size="34" fill="#f0f0f0">3</text>
      <text y="41" text-anchor="middle" font-size="19" fill="#cfcfcf">psi</text>
    </g>

    <!-- Rate gauge -->
    <g class="gauge rate-gauge" transform="translate(863 155)">
      <use href="#dial-body"/>
      <use href="#dial-ticks"/>
      <path d="M -59.4 59.4 A 84 84 0 1 1 59.4 59.4" fill="none" stroke="var(--green)" stroke-width="12"
            pathLength="270" stroke-dasharray="0 134 12 400"/>
      <g font-size="9" fill="#d0d0d0" text-anchor="middle">
        <text transform="rotate(-135) translate(0 -99)">-40</text>
        <text transform="rotate(-101.25) translate(0 -99)">-33</text>
        <text transform="rotate(-67.5) translate(0 -99)">-25</text>
        <text transform="rotate(-33.75) translate(0 -99)">-18</text>
        <text transform="rotate(0) translate(0 -99)">-10</text>
        <text transform="rotate(33.75) translate(0 -99)">-3</text>
        <text transform="rotate(67.5) translate(0 -99)">5</text>
        <text transform="rotate(101.25) translate(0 -99)">13</text>
        <text transform="rotate(135) translate(0 -99)">20</text>
      </g>
      <use href="#spec-pointer"/>
      <text y="-28" text-anchor="middle" font-size="19" fill="#dcdcdc">RATE</text>
      <rect x="-61" y="-22" width="122" height="45" rx="8" fill="url(#digit-cells)"/>
      <text x="-8" y="12" text-anchor="middle" class="digits" font-size="34" fill="#f0f0f0">-8</text>
      <rect x="15" y="6" width="5" height="5" fill="#f0f0f0"/>
      <text x="36" y="12" text-anchor="middle" class="digits" font-size="34" fill="#f0f0f0">1</text>
      <text y="41" text-anchor="middle" font-size="19" fill="#cfcfcf">psi / min</text>
    </g>

    <!-- Trend gauge -->
    <g class="gauge trend-gauge" transform="translate(1100 155)">
      <use href="#dial-body"/>
      <use href="#dial-ticks"/>
      <line x1="0" y1="-79" x2="0" y2="-91" stroke="var(--green)" stroke-width="2"/>
      <g font-size="9" fill="#d0d0d0" text-anchor="middle">
        <text transform="rotate(-135) translate(0 -99)">-100</text>
        <text transform="rotate(-101.25) translate(0 -99)">-75</text>
        <text transform="rotate(-67.5) translate(0 -99)">-50</text>
        <text transform="rotate(-33.75) translate(0 -99)">-25</text>
        <text transform="rotate(0) translate(0 -99)">0</text>
        <text transform="rotate(33.75) translate(0 -99)">25</text>
        <text transform="rotate(67.5) translate(0 -99)">50</text>
        <text transform="rotate(101.25) translate(0 -99)">75</text>
        <text transform="rotate(135) translate(0 -99)">100</text>
      </g>
      <use href="#spec-pointer"/>
      <text y="-28" text-anchor="middle" font-size="19" fill="#dcdcdc">TREND</text>
      <rect x="-62" y="-22" width="124" height="45" rx="10" fill="#3a3a3a"/>
      <text y="7" text-anchor="middle" font-size="19" fill="#f0f0f0">Improving</text>
    </g>

    <!-- Hold percentage -->
    <g class="hold-meter">
      <rect x="1222" y="47" width="106" height="215" rx="10" fill="var(--panel-dark)"/>
      <rect x="1258" y="62" width="12" height="162" fill="#3a3a3a"/>
      <rect x="1258" y="130" width="12" height="94" fill="var(--cyan)"/>
      <line x1="1272" y1="62" x2="1272" y2="224" stroke="#777" stroke-width="1"/>
      <g stroke="#777" stroke-width="1">
        <line x1="1272" y1="62" x2="1277" y2="62"/>
        <line x1="1272" y1="102.5" x2="1277" y2="102.5"/>
        <line x1="1272" y1="143" x2="1277" y2="143"/>
        <line x1="1272" y1="183.5" x2="1277" y2="183.5"/>
        <line x1="1272" y1="224" x2="1277" y2="224"/>
      </g>
      <g font-size="8" fill="#cfcfcf">
        <text x="1279" y="65">100</text>
        <text x="1279" y="105">75</text>
        <text x="1279" y="146">50</text>
        <text x="1279" y="186">25</text>
        <text x="1279" y="227">0</text>
      </g>
      <text x="1275" y="249" text-anchor="middle" font-size="18" fill="#dcdcdc">HOLD %</text>
    </g>

    <!-- Chart -->
    <g class="pressure-chart">
      <rect x="95" y="288" width="1182" height="475" fill="var(--plot)"/>
      <rect x="95" y="394" width="1182" height="197" fill="var(--band)"/>
      <rect x="828" y="288" width="449" height="475" fill="#ffffff" fill-opacity="0.035"/>

      <g stroke="#4a4a4a" stroke-width="1" stroke-dasharray="3 4">
        <line x1="180" y1="288" x2="180" y2="763"/>
        <line x1="405" y1="288" x2="405" y2="763"/>
        <line x1="629" y1="288" x2="629" y2="763"/>
        <line x1="854" y1="288" x2="854" y2="763"/>
        <line x1="1079" y1="288" x2="1079" y2="763"/>
        <line x1="95" y1="339" x2="1277" y2="339"/>
        <line x1="95" y1="429" x2="1277" y2="429"/>
        <line x1="95" y1="519" x2="1277" y2="519"/>
        <line x1="95" y1="610" x2="1277" y2="610"/>
        <line x1="95" y1="700" x2="1277" y2="700"/>
      </g>

      <rect x="828" y="289" width="449" height="20" fill="var(--accent-deep)"/>
      <text x="1052" y="307" text-anchor="middle" font-size="21" fill="#f2f2f2">1 Min Test Period</text>
      <line x1="828" y1="289" x2="828" y2="763" stroke="var(--accent-deep)" stroke-width="1.5"/>

      <line x1="95" y1="763" x2="1277" y2="763" stroke="#555" stroke-width="1"/>
      <line x1="95" y1="766" x2="1277" y2="766" stroke="#555" stroke-width="4" stroke-dasharray="1 44.9"/>

      <g font-size="12" fill="var(--pink)" text-anchor="end">
        <text x="86" y="343">30</text>
        <text x="86" y="433">25</text>
        <text x="86" y="523">20</text>
        <text x="86" y="614">15</text>
        <text x="86" y="704">10</text>
      </g>
      <text transform="translate(57 526) rotate(-90)" text-anchor="middle" font-size="14" fill="var(--pink)">Temperature</text>

      <g font-size="11" fill="#4aa6e8">
        <text x="1287" y="319">1200</text>
        <text x="1287" y="359">1100</text>
        <text x="1287" y="398">1000</text>
        <text x="1287" y="437">900</text>
        <text x="1287" y="476">800</text>
        <text x="1287" y="516">700</text>
        <text x="1287" y="555">600</text>
        <text x="1287" y="594">500</text>
        <text x="1287" y="634">400</text>
        <text x="1287" y="673">300</text>
        <text x="1287" y="712">200</text>
        <text x="1287" y="752">100</text>
      </g>
      <text transform="translate(1325 526) rotate(-90)" text-anchor="middle" font-size="14" fill="#4aa6e8">Pressure</text>

      <g font-size="12" fill="#cfcfcf" text-anchor="middle">
        <text x="180" y="784">22:04:30</text>
        <text x="405" y="784">22:05:00</text>
        <text x="629" y="784">22:05:30</text>
        <text x="854" y="784">22:06:00</text>
        <text x="1079" y="784">22:06:30</text>
      </g>

      <path d="M 95 339 L 470 339 C 490 339 500 334 520 333 L 828 334 L 1088 336.5" fill="none" stroke="var(--pink)" stroke-width="2"/>

      <path d="M 474 760 L 479 742 L 483 731 L 486 712 L 490 690 L 493 672 L 496 650 L 500 624 L 503 600 L 506 572 L 509 548 L 512 528 L 515 510 L 518 490 L 521 472 L 524 456 L 526 452 L 828 456 L 957 457.5"
            fill="none" stroke="var(--accent)" stroke-width="3.5" stroke-linejoin="round"/>
      <line x1="957" y1="457.5" x2="1088" y2="458" stroke="var(--green)" stroke-width="3.5"/>
      <line x1="1088" y1="458" x2="1277" y2="459" stroke="var(--green)" stroke-width="1.5" stroke-dasharray="10 8"/>
      <circle cx="957" cy="457.5" r="3" fill="var(--accent)"/>
      <circle cx="1088" cy="458" r="3" fill="var(--accent)"/>
      <circle cx="1277" cy="459" r="3.5" fill="var(--green)"/>

      <g font-size="17" fill="var(--accent)" text-anchor="middle">
        <text x="794" y="428">P1</text>
        <text x="802" y="450">844.3</text>
        <text x="924" y="430">P2</text>
        <text x="931" y="451">841.4</text>
        <text x="1054" y="430">P3</text>
        <text x="1062" y="452">839.0</text>
      </g>
      <text x="1256" y="449" text-anchor="middle" font-size="18" fill="var(--green)">836</text>

      <g class="start-callout">
        <rect x="370" y="713" width="92" height="29" rx="4" fill="var(--callout)"/>
        <path d="M 398 741 L 405 758 L 412 741 Z" fill="var(--callout)"/>
        <text x="416" y="732" text-anchor="middle" font-size="11" font-weight="700" fill="#111">Start operation</text>
      </g>
      <path d="M 1082 773 L 1087 766 L 1092 773 Z" fill="var(--marker)"/>
    </g>
  </svg>

  <div class="control-panel">
    <div class="control-button" style="top:5px">Screen Shot</div>
    <div class="control-button" style="top:61px">Heave Cancel</div>
    <div class="control-button active" style="top:118px">Prediction</div>
    <div class="control-button" style="top:174px">Zoom</div>
    <div class="control-button" style="top:230px">Snap Halo</div>
    <div class="control-button" style="top:286px">Reset View</div>
  </div>
  <div class="control-panel lower">
    <div class="control-button" style="top:5px; height:54px">Lock Hold<br>Period</div>
    <div class="control-button disabled" style="top:68px">Publish</div>
  </div>

</div>
</div>
</body>
</html>
```